Refresh of Business Card Design

Want to refresh the business card design with the new logo while adhering to style guide as attached. Would like to match feel of website www.durmackvinex.com

```html
<!DOCTYPE html>
<html lang="en">
<head>
<meta charset="utf-8">
<title>Durmack Vinex – Business Card</title>
<link href="https://fonts.googleapis.com/css2?family=Open+Sans:wght@400;600;700&display=swap" rel="stylesheet">
<style>
  :root {
    --page-bg: #222222;
    --card-black: #060709;
    --card-red-core: #c4161c;
    --card-red-mid: #8e1014;
    --card-red-edge: #5e0c10;
    --accent-red: #e3202a;
    --text-white: #ffffff;
    --rule-grey: #8a8a8a;
    --mark-silver: #d9d9d9;
  }
  html, body {
    margin: 0;
    padding: 0;
    width: 1200px;
    height: 780px;
    overflow: hidden;
    background: var(--page-bg);
    font-family: "Open Sans", Arial, sans-serif;
  }
  .canvas {
    position: relative;
    width: 1200px;
    height: 780px;
    display: flex;
    align-items: center;
    justify-content: center;
    gap: 40px;
  }
  .card {
    position: relative;
    width: 560px;
    height: 320px;
    box-sizing: border-box;
    overflow: hidden;
  }

  /* Back of card: contact side */
  .card-back {
    background: var(--card-black);
    color: var(--text-white);
  }
  .back-brand {
    position: absolute;
    left: 0;
    top: 0;
    width: 235px;
    height: 320px;
    display: flex;
    align-items: center;
    justify-content: center;
    gap: 10px;
  }
  .brand-dot {
    width: 14px;
    height: 14px;
    border-radius: 50%;
    background: var(--accent-red);
    flex: none;
  }
  .brand-name {
    font-weight: 700;
    font-size: 19px;
    letter-spacing: 1.5px;
    color: var(--text-white);
    white-space: nowrap;
  }
  .divider {
    position: absolute;
    left: 245px;
    top: 40px;
    width: 1px;
    height: 150px;
    background: linear-gradient(to bottom, transparent, var(--rule-grey) 30%, var(--rule-grey) 70%, transparent);
  }
  .person {
    position: absolute;
    left: 272px;
    top: 46px;
  }
  .person-name {
    margin: 0;
    font-size: 30px;
    font-weight: 700;
    line-height: 1;
  }
  .person-name .first { color: var(--accent-red); }
  .person-name .last { color: var(--text-white); }
  .person-role {
    margin: 4px 0 0;
    font-size: 13px;
    font-weight: 600;
  }
  .contacts {
    list-style: none;
    margin: 22px 0 0;
    padding: 0;
    font-size: 12.5px;
  }
  .contacts li {
    display: flex;
    align-items: center;
    gap: 8px;
    margin-bottom: 5px;
  }
  .contacts svg {
    width: 13px;
    height: 13px;
    flex: none;
    fill: var(--accent-red);
  }
  .address {
    position: absolute;
    left: 245px;
    top: 228px;
    margin: 0;
    font-style: normal;
    font-size: 13px;
    line-height: 1.45;
  }

  /* Front of card: brand side */
  .card-front {
    background: radial-gradient(ellipse 55% 70% at 50% 52%, var(--card-red-core) 0%, var(--card-red-mid) 45%, var(--card-red-edge) 100%);
    display: flex;
    align-items: center;
    justify-content: center;
    gap: 14px;
  }
  .card-front .brand-dot {
    width: 24px;
    height: 24px;
    background: var(--text-white);
  }
  .card-front .brand-name {
    font-size: 34px;
    letter-spacing: 3px;
  }
</style>
</head>
<body>
<main class="canvas">
  <section class="card card-back" aria-label="Business card, contact side">
    <div class="back-brand">
      <span class="brand-dot"></span>
      <span class="brand-name">DURMACK VINEX</span>
    </div>
    <div class="divider"></div>
    <div class="person">
      <h1 class="person-name"><span class="first">Wade</span> <span class="last">Kessler</span></h1>
      <p class="person-role">Sales</p>
      <ul class="contacts">
        <li>
          <svg viewBox="0 0 24 24" aria-hidden="true"><path d="M6.6 10.8a15.1 15.1 0 0 0 6.6 6.6l2.2-2.2a1 1 0 0 1 1-.25 11.4 11.4 0 0 0 3.6.57 1 1 0 0 1 1 1V20a1 1 0 0 1-1 1A17 17 0 0 1 3 4a1 1 0 0 1 1-1h3.5a1 1 0 0 1 1 1c0 1.25.2 2.45.57 3.57a1 1 0 0 1-.25 1z"/></svg>
          555.010.4827
        </li>
        <li>
          <svg viewBox="0 0 24 24" aria-hidden="true"><path d="M12 2a10 10 0 1 0 0 20 10 10 0 0 0 0-20zm6.9 6h-2.9a15.6 15.6 0 0 0-1.4-3.6A8 8 0 0 1 18.9 8zM12 4a14 14 0 0 1 1.9 4h-3.8A14 14 0 0 1 12 4zM4.3 14a8 8 0 0 1 0-4h3.4a16.5 16.5 0 0 0 0 4zm.8 2h2.9a15.6 15.6 0 0 0 1.4 3.6A8 8 0 0 1 5.1 16zM8 8H5.1a8 8 0 0 1 4.3-3.6A15.6 15.6 0 0 0 8 8zm4 12a14 14 0 0 1-1.9-4h3.8A14 14 0 0 1 12 20zm2.3-6H9.7a14.7 14.7 0 0 1 0-4h4.6a14.7 14.7 0 0 1 0 4zm.3 5.6a15.6 15.6 0 0 0 1.4-3.6h2.9a8 8 0 0 1-4.3 3.6zm1.7-5.6a16.5 16.5 0 0 0 0-4h3.4a8 8 0 0 1 0 4z"/></svg>
          www.durmackvinex.com
        </li>
        <li>
          <svg viewBox="0 0 24 24" aria-hidden="true"><path d="M3 5h18a1 1 0 0 1 1 1v12a1 1 0 0 1-1 1H3a1 1 0 0 1-1-1V6a1 1 0 0 1 1-1zm1 2.4V17h16V7.4l-8 5.3z M5.2 7 12 11.5 18.8 7z"/></svg>
          wkessler@durmackvinex.com
        </li>
      </ul>
    </div>
    <address class="address">
      P.O. Box 40218 Harlow, TX 79802<br>
      412 Ridgeview Dr Calder, Texas 79345
    </address>
  </section>

  <section class="card card-front" aria-label="Business card, brand side">
    <span class="brand-dot"></span>
    <span class="brand-name">DURMACK VINEX</span>
  </section>
</main>
</body>
</html>
```